Californian Mexican restaurant menu design

We looking for a designer who can design an original menu design for a mexican restaurant. We are not looking for a design that is "cliché méxican style" or a menu that is too simple and not creative.

- tri fold colour menu back and front
° the menu items need to stay by categories (Burritos, quesadillas, tacos etc..)

Industry/Entity Type

restaurant

```html
<!DOCTYPE html>
<html lang="fr">
<head>
<meta charset="utf-8">
<title>Menu – Cuisine mexicaine californienne</title>
<link rel="stylesheet" href="https://fonts.googleapis.com/css2?family=Amatic+SC:wght@400;700&family=Roboto:ital,wght@0,400;0,500;1,400&display=swap">
<style>
:root{
  --paper:#fdf5e4;
  --band:#6b0a0a;
  --band-ink:#fdf5e4;
  --title:#7a0f14;
  --body:#6a6a6a;
  --photo-warm:#b6834f;
  --photo-dark:#5a4636;
  --photo-light:#e7d8c0;
  --deco:#d8962c;
}
*{box-sizing:border-box;margin:0;padding:0}
html,body{width:1200px;height:853px;overflow:hidden;background:var(--paper)}
body{position:relative;font-family:"Roboto",Arial,sans-serif}
.band{position:absolute;background:var(--band);color:var(--band-ink);
  font-family:"Amatic SC","Arial Narrow",sans-serif;font-weight:400;font-size:25px;
  display:flex;align-items:center;padding-left:26px;letter-spacing:.5px}
.band .deco{position:absolute;right:4px;top:50%;transform:translateY(-50%);
  width:72px;height:40px;border-radius:50%;
  background:radial-gradient(circle at 50% 45%,var(--deco),#a33a18)}
.photo{position:absolute}
.section{position:absolute}
.item{margin-bottom:3px}
.item-head{display:flex;align-items:baseline;color:var(--title);font-weight:500;font-size:12px;line-height:15px}
.leader{flex:1;border-bottom:2px dotted var(--title);margin:0 4px 3px;opacity:.8}
.desc{color:var(--body);font-style:italic;font-size:11.4px;line-height:15.2px;text-align:justify}
.note{position:absolute;left:406px;top:787px;width:391px;height:40px;background:var(--band);
  color:var(--band-ink);font-style:italic;font-size:12.5px;line-height:16px;padding:3px 0 0 16px}
.note .deco{position:absolute;right:10px;top:-6px;width:82px;height:48px;border-radius:50%;
  background:radial-gradient(circle,var(--deco),#b3541e)}
.promises{position:absolute;left:838px;top:716px;width:312px}
.promise{display:flex;gap:18px;margin-bottom:7px}
.promise svg{flex:none;width:26px;height:26px}
.promise p{color:var(--title);font-weight:500;font-size:10.5px;line-height:13.5px;text-align:justify}
</style>
</head>
<body>

<!-- Left panel -->
<div class="band" style="left:0;top:18px;width:378px;height:39px;">Appetizers<span class="deco" role="img" aria-label="Illustration d'une assiette de taquitos"></span></div>
<div class="section" style="left:43px;top:65px;width:340px;">
  <div class="item"><div class="item-head">TAQUITOS<span class="leader"></span>13€</div><p class="desc">Galettes de maïs garnies de poulet, fromage et piments jalapeños. Accompagnées de guacamole.</p></div>
  <div class="item"><div class="item-head">VEGAN TAQUITOS<span class="leader"></span>13€</div><p class="desc">Galettes de maïs garnies avec des haricots noirs ecrasés, oignons, coriandre et jalapenos. Servie avec du guacamole &amp; salsa roja.</p></div>
  <div class="item"><div class="item-head">RUDY'S FAVORITE<span class="leader"></span>13€</div><p class="desc">Galettes de blé frite garnies de boeuf effiloché, fromages et piment jalapeños. Accompagnées de guacamole.</p></div>
  <div class="item"><div class="item-head">JALAPEÑOS POPPERS<span class="leader"></span>13€</div><p class="desc">Piments jalapeños frais farcis et gratinés de trois fromages.</p></div>
  <div class="item"><div class="item-head">DIP SEA<span class="leader"></span>13€</div><p class="desc">Poulpe cuit a bassse temperature pendant six heures.</p></div>
  <div class="item"><div class="item-head">CHIPS, SALSA &amp; GUACAMOLE<span class="leader"></span>13€</div></div>
</div>

<div class="band" style="left:0;top:322px;width:378px;height:42px;">Signature Burritos<span class="deco" role="img" aria-label="Illustration d'un burrito"></span></div>
<div class="photo" style="left:43px;top:364px;width:336px;height:100px;background:linear-gradient(160deg,var(--photo-light),var(--photo-warm) 55%,var(--photo-dark));" role="img" aria-label="Photo de burritos garnis de haricots et légumes"></div>
<div class="section" style="left:43px;top:470px;width:340px;">
  <div class="item"><div class="item-head">OUTLAW(épicé sur demande)<span class="leader"></span>17 €</div><p class="desc">Poulet braisé aux piments de pasilla, mélange de poivrons et oignons sautés à la plancha, riz et sauce à l'avocat. Gratiné avec du fromage et une sauce enchilada. Accompagnée d'une salade composée.</p></div>
  <div class="item"><div class="item-head">I LOVE CHEESE<span class="leader"></span>17 €</div><p class="desc">Galette de blé frtie. Garnie de poulet braisé, fromage cheddar, mozzarella et piments jalapeño. Servie avec du guacamole, riz et haricots noirs ou purée de haricots roses.</p></div>
  <div class="item"><div class="item-head">THE ZEN<span class="leader"></span>17 €</div><p class="desc">Boeuf braisé pendant 12H dans une sauce Mole, riz et sauce à l'avocat. Gratinée avec du fromage cheddar, sauce enchilada. Accompagnée d'une salade composée.</p></div>
  <div class="item"><div class="item-head">GIVE ME LOVE (épicé sur demande)<span class="leader"></span>17 €</div><p class="desc">Boeuf braisé pendant 12h, haricots noirs, riz, sauce à l'avocat et salsa de tomates. Gratinée avec du fromage et une sauce enchilada. Accompagnée d'une salade composée.</p></div>
  <div class="item"><div class="item-head">GREEN PEACE (épicé sur demande)<span class="leader"></span>17 €</div><p class="desc">Mélange de poivrons et oignons sautés à la plancha, haricots noirs, guacamole, salsa et riz. Gratinée avec du fromage cheddar et sauce enchilada . Accompagnée d'une salade composée.</p></div>
</div>

<!-- Middle panel -->
<div class="band" style="left:421px;top:19px;width:346px;height:40px;">Nachos<span class="deco" role="img" aria-label="Illustration de chips de nachos"></span></div>
<div class="photo" style="left:421px;top:59px;width:346px;height:116px;background:radial-gradient(ellipse at 45% 55%,#9bb04a 0,#c9902f 22%,#6b4a32 55%,#3b3633 100%);" role="img" aria-label="Photo d'une assiette de nachos au guacamole et viande hachée"></div>
<div class="section" style="left:424px;top:181px;width:342px;">
  <div class="item"><div class="item-head">Big CRUNCH<span class="leader"></span>18 €</div><p class="desc">Chips de maïs maison recouvertes de cheddar fondu, pico de gallo), haricots noirs, poulet mariné et grillé, piments jalapeño pickle, guacamole et crème montée au citron vert.</p></div>
  <div class="item"><div class="item-head">VEGGIE Le même mais Veggie!<span class="leader"></span>17 €</div></div>
  <div class="item"><div class="item-head">Big CRUNCH CHORIZO<span class="leader"></span>18 €</div><p class="desc">Chips de maïs maison recouvertes de cheddar fondu, pico de gallo, haricots noirs, piments jalapeño pickle, guacamole et crème montée au citron vert.</p></div>
</div>

<div class="band" style="left:421px;top:326px;width:359px;height:40px;">Salades<span class="deco" role="img" aria-label="Illustration d'un bol de haricots rouges"></span></div>
<div class="section" style="left:424px;top:373px;width:342px;">
  <div class="item"><div class="item-head">THE TACO SALADE<span class="leader"></span>17 €</div><p class="desc">Poulet mariné et grillé, pico de gallo, haricots noirs, fromage cheddar, crème fraiche et guacamole. Servie dans une galette de blé croustillante.</p></div>
  <div class="item"><div class="item-head">MANGO SALAD<span class="leader"></span>16,5€</div><p class="desc">Salade verte composée de mangue fraiche, oignons, poivrons rouge et escalope de poulet marinée au jus d'orange et jus d'ananas. Servie dans une galette de blé croustillante.</p></div>
</div>

<div class="band" style="left:421px;top:514px;width:359px;height:41px;">Quesadillas<span class="deco" role="img" aria-label="Illustration de parts de quesadilla"></span></div>
<div class="section" style="left:430px;top:561px;width:340px;">
  <div class="item"><div class="item-head">ORIGINAL<span class="leader"></span>17 €</div><p class="desc">Galette de blé toastée et garnie de poulet braisé aux piments pasillas, fromage cheddar, mozzarela et pico de gallo. Servie avec du riz, haricots noirs ou purée de haricots roses, guacamole et pico de gallo.</p></div>
  <div class="item"><div class="item-head">THE MEXICAN CHORIZO<span class="leader"></span>17 €</div><p class="desc">Galette de blé toastée et garnie de chorizo mexicain maison et fromage cheddar et mozzarela. Accompagnée d'une salade composée.</p></div>
  <div class="item"><div class="item-head">VEGGIE<span class="leader"></span>16,5 €</div><p class="desc">Galette de blé toastée et garnie d'un mélange de poivrons et oignons sautés à la plancha, fromage cheddar, mozzarela et haricots noirs. Servie avec du riz, haricots noirs ou purée de haricots roses, guacamole et pico de gallo.</p></div>
</div>

<div class="note">Nous fabriquons nos galettes de blé sur<br>place et à la commande<span class="deco" role="img" aria-label="Illustration d'une pile de galettes"></span></div>

<!-- Right panel -->
<div class="band" style="left:805px;top:19px;width:395px;height:40px;padding-left:38px;">Baja Fish Tacos<span class="deco" role="img" aria-label="Illustration d'un taco"></span></div>
<div class="section" style="left:823px;top:67px;width:340px;">
  <div class="item"><div class="item-head">BAJA CALIFORNIA<span class="leader"></span>17 €</div><p class="desc">Thon albacore mi-cuit, mayonnaise au piment chipotle maison, canbrerries , avocats et iceberg. Accompagnés d'une salade composée et d'un pudding au maïs.</p></div>
  <div class="item"><div class="item-head">RED SNAPPER<span class="leader"></span>17 €</div><p class="desc">Beignets de filets de rouget, sauce à l'orange. Servi ave un Mélange d'oranges, poivrons, oignons rouge et jalepnos. Accompagnés d'une salade composée et d'un pudding au maïs.</p></div>
  <div class="item"><div class="item-head">FISHERMAN<span class="leader"></span>17 €</div><p class="desc">Gambas flambées à la tequila, salsa de mangues fraiches, oignons et poivrons rouges. Accompagnés d'une salade composée et d'un udding au maïs.</p></div>
</div>

<div class="band" style="left:805px;top:287px;width:395px;height:42px;padding-left:38px;">Meat Tacos<span class="deco" role="img" aria-label="Illustration d'un taco garni"></span></div>
<div class="section" style="left:823px;top:334px;width:340px;">
  <div class="item"><div class="item-head">SURF CITY<span class="leader"></span>16 €</div><p class="desc">Escalopes de poulet marinées dans un cocktail de jus d'orange, ananas et tequila. Servies avec de la salade iceberg, pico de gallo, fromage cheddar et sauce à l'avocat. accompagnées de riz et purée de haricots roses.</p></div>
  <div class="item"><div class="item-head">LITTLE PIG<span class="leader"></span>16,5 €</div><p class="desc">Poitrine de porc braisée pendant 4 heures dans une sauce aux piments Chipotle fumés. Servie avec du chou rouge en pickles. Accompagnée de riz et purée de haricots roses.</p></div>
  <div class="item"><div class="item-head">THE SHEPHERD<span class="leader"></span>16,5€</div><p class="desc">Filet d'agneau mariné dans une sauce Adobo, salade iceberg, oignons rouges en pickles et sauce à l'avocats. Accompagné de riz et purée de haricots roses.</p></div>
</div>
<div class="photo" style="left:805px;top:539px;width:395px;height:163px;background:linear-gradient(120deg,#d9c9a8,#e2b94a 35%,#9a5a2e 60%,#f1ebe0 85%);" role="img" aria-label="Photo de tacos croustillants garnis de viande, salade et fromage"></div>

<div class="promises">
  <div class="promise">
    <svg viewBox="0 0 26 26" fill="none" stroke="#222" stroke-width="1.8"><path d="M6 10 13 4l7 6M8 14h10M6 18h14M6 22h14"/></svg>
    <p>Chez nous, tous les plats sont faits maison à partir de produits frais. Nous réalisons nos tortillas de blé sur place et à la commande</p>
  </div>
  <div class="promise">
    <svg viewBox="0 0 26 26" fill="none" stroke="#666" stroke-width="1.4"><path d="M7 8h12l1 15H6z"/><path d="M9 8 10 4h6l1 4"/><rect x="9" y="13" width="8" height="5" rx="1"/></svg>
    <p>Nous mettons à votre disposition un Doggy Bag si vous n'avez pas fini votre plat</p>
  </div>
  <div class="promise">
    <svg viewBox="0 0 26 26" fill="#222"><path d="M3 9h16l3-2 2 2-2 3v6h-2v4h-2v-4H9v4H7v-4H5v-5L3 12z"/></svg>
    <p>Toutes nos viandes bovines, et notre volaille proviennent exclusivement d'élevage de la région Auvergne Rhône Alpes</p>
  </div>
</div>

</body>
</html>
```